Lucia Verena a furniture, interior design and home decor Brand

I need complete stationary for a new brand, business card, postcard, letter head, shipping envelopes, tissue paper, etc... I would like to use copper foil on some of these items. I have a logo design. I would like to see

Target Market(s)

Furniture,Interior Design & Home Decor

Industry/Entity Type

Interior Design

Colors
606060
7f7f7f

Requirements
Must have
• My signature style is spanish medeterrenean, my brand colors is charcoal gray with copper. Would love to see a wrought iron panel illustration created, I have attahced a few samples of wrought iron illustration I am attracted to, also an example of packing that has the pattern in foil.
Should not have
• Will not be using the word Design, only Lucia Verena and LV icon

```html
<!DOCTYPE html>
<html lang="en">
<head>
<meta charset="utf-8">
<title>Lucia Verena — Business Card</title>
<link rel="stylesheet" href="https://fonts.googleapis.com/css2?family=Open+Sans:wght@400;600;700&display=swap">
<style>
  :root {
    --backdrop: #e9e9e9;
    --card: #ffffff;
    --copper: #d9622a;
    --copper-light: #f2a47c;
    --charcoal: #4f4f4f;
    --gray: #606060;
    --gray-soft: #7f7f7f;
  }
  * { box-sizing: border-box; margin: 0; padding: 0; }
  html, body {
    width: 1200px; height: 1000px; overflow: hidden;
    background: var(--backdrop);
    font-family: "Open Sans", Arial, sans-serif;
  }
  .stage {
    position: relative; width: 1200px; height: 1000px;
    display: flex; flex-direction: column; align-items: center;
    justify-content: center; gap: 48px;
  }
  .card {
    position: relative; width: 700px; height: 400px;
    background: var(--card);
    box-shadow: 0 6px 22px rgba(0,0,0,0.12);
    overflow: hidden;
  }
  /* Back side */
  .card-back {
    display: flex; align-items: center; justify-content: center; gap: 18px;
  }
  .card-back .mark-circle {
    width: 56px; height: 56px; border: 2px solid var(--copper); border-radius: 50%;
  }
  .card-back .brand-name {
    font-size: 40px; font-weight: 400; color: var(--copper); letter-spacing: 1px;
  }
  /* Front side */
  .copper-band {
    position: absolute; left: 70px; top: 0; width: 96px; height: 100%;
    background: linear-gradient(180deg, var(--copper) 0%, var(--copper-light) 38%, var(--copper) 100%);
  }
  .brand-lockup {
    position: absolute; left: 86px; top: 34px;
    display: flex; align-items: center; gap: 14px;
  }
  .brand-lockup .mark-circle {
    width: 68px; height: 68px; border-radius: 50%;
    border: 2px solid var(--copper); background: var(--card);
  }
  .brand-lockup .brand-name {
    font-size: 30px; font-weight: 400; color: var(--copper);
  }
  .contact-icons {
    position: absolute; left: 100px; top: 180px; width: 36px;
    display: flex; flex-direction: column; align-items: center;
  }
  .contact-icons svg { display: block; fill: #ffffff; }
  .icon-pin { margin-bottom: 66px; }
  .icon-phone, .icon-mobile, .icon-mail { margin-bottom: 12px; }
  .contact-details {
    position: absolute; left: 196px; top: 196px;
    color: var(--charcoal); font-size: 19px; line-height: 25px;
  }
  .contact-details .address { margin-bottom: 12px; }
  .person {
    position: absolute; right: 44px; top: 92px; text-align: right;
  }
  .person .name {
    font-size: 25px; font-weight: 700; color: var(--copper); letter-spacing: 0.5px;
  }
  .person .title {
    font-size: 18px; font-weight: 400; color: var(--gray); letter-spacing: 0.5px;
  }
</style>
</head>
<body>
<main class="stage">
  <section class="card card-back" aria-label="Business card back">
    <span class="mark-circle"></span>
    <span class="brand-name">Lucia Verena</span>
  </section>

  <section class="card card-front" aria-label="Business card front">
    <div class="copper-band"></div>
    <div class="brand-lockup">
      <span class="mark-circle"></span>
      <span class="brand-name">Lucia Verena</span>
    </div>

    <div class="contact-icons" aria-hidden="true">
      <svg class="icon-pin" width="14" height="20" viewBox="0 0 14 20"><path d="M7 0C3.1 0 0 3.1 0 7c0 5 7 13 7 13s7-8 7-13c0-3.9-3.1-7-7-7zm0 9.5A2.5 2.5 0 1 1 7 4.5a2.5 2.5 0 0 1 0 5z"/></svg>
      <svg class="icon-phone" width="20" height="16" viewBox="0 0 20 16"><path d="M2 4c0-2 3-4 8-4s8 2 8 4v2h-4V4H6v2H2zM4 7h12l2 9H2z"/></svg>
      <svg class="icon-mobile" width="12" height="20" viewBox="0 0 12 20"><path d="M2 0h8a2 2 0 0 1 2 2v16a2 2 0 0 1-2 2H2a2 2 0 0 1-2-2V2a2 2 0 0 1 2-2zm0 3v12h8V3z"/></svg>
      <svg class="icon-mail" width="20" height="14" viewBox="0 0 20 14"><path d="M0 0h20v2L10 8 0 2zM0 4l10 6 10-6v10H0z"/></svg>
      <svg class="icon-web" width="18" height="18" viewBox="0 0 18 18"><circle cx="9" cy="9" r="8" fill="none" stroke="#fff" stroke-width="2"/><path d="M1 9h16M9 1c-4 4-4 12 0 16M9 1c4 4 4 12 0 16" fill="none" stroke="#fff" stroke-width="1.5"/></svg>
    </div>

    <div class="contact-details">
      <p class="address">2417 Alder Crest Lane<br>Brookhaven, NY 11719</p>
      <p class="phone">631 502 7184</p>
      <p class="mobile">631 778 2093</p>
      <p class="email">hello@luciaverena.com</p>
      <p class="web">www.luciaverena.com</p>
    </div>

    <div class="person">
      <p class="name">LUCIA VERENA</p>
      <p class="title">PRESIDENT</p>
    </div>
  </section>
</main>
</body>
</html>
```